Web Page for marketing online agency

We are an online marketing agency that is acing the direct response model. We engage with our customers throughout different marketing techniques as research copy-writing, advertisements and content writing. We would need a website design that will have four main aspects: The Vision; stating who we are, The Mission; stating what we do, The Team And It's Values, and a Contact Form. For this design we would want a sharp, clean and smart approach, with illustrated elements or suggestive images. You can use the attached copy, the logo, the USP and the motto. Please integrate them as you see fit while keeping in mind the previous needs and copy. This website is going to be our connection with our possible partners, future colleagues and even our clients. You may submit a design for one page or integrate the 4 different aspects on separate web pages.
Target Market(s)
business partners, future employees, age range 25-60
Industry/Entity Type
Direct Marketing
Number of Pages Required
1 page
Requirements
Must have
- Menu / Header
- 4 Parts or 4 Pages including: vision, mission, team, contact
- Logo
- Motto: Direct Brilliance
- USP: We help people help themselves.
- The copy attached
Nice to have
- Representative illustrated images or elements
Should not have
- A boring design, classical design - Pagequill like

```html
<!DOCTYPE html>
<html lang="en">
<head>
<meta charset="utf-8">
<title>BrightWell — Direct Brilliance</title>
<link rel="stylesheet" href="https://fonts.googleapis.com/css2?family=Roboto:ital,wght@0,300;0,400;0,500;0,700;0,900;1,500&display=swap">
<style>
:root{
  --blue:#2e9fd9;
  --blue-deep:#1f7fb8;
  --blue-dark:#17557e;
  --ink:#1d1d1d;
  --text:#3c3c3c;
  --muted:#6b6b6b;
  --white:#ffffff;
  --field-line:#8fc8ea;
}
*{margin:0;padding:0;box-sizing:border-box}
html,body{width:1200px;height:5187px;overflow:hidden;background:var(--white)}
body{font-family:"Roboto",Arial,sans-serif;color:var(--text)}
.page{position:relative;width:1200px;height:5187px;overflow:hidden}
.abs{position:absolute}
svg.shape{position:absolute;left:0;display:block}

/* hero */
.hero-photo{left:0;top:0;width:1200px;height:900px;
  background:linear-gradient(160deg,#d9d4cc 0%,#b9b1a6 35%,#8e877e 60%,#cfc9c1 100%)}
.brand{left:0;top:62px;width:1200px;text-align:center}
.brand-name{font-size:42px;font-weight:500;color:var(--blue-dark);letter-spacing:.5px}
.brand-dot{display:inline-block;width:22px;height:22px;border-radius:50%;background:var(--blue);margin-left:8px;vertical-align:6px}
.nav{left:0;top:152px;width:1200px;display:flex;justify-content:center;gap:34px}
.nav a{font-size:17px;font-weight:700;color:var(--ink);text-decoration:none;letter-spacing:.3px}
.usp{left:0;top:318px;width:1200px;text-align:center;font-size:54px;font-weight:900;color:var(--white);letter-spacing:.5px}
.motto{left:0;top:440px;width:1200px;text-align:center;font-size:36px;font-style:italic;font-weight:500;color:var(--white)}
.motto b{font-size:60px;vertical-align:-8px;font-weight:700}
.chevron{left:570px;top:676px}

/* section headings */
.h2{font-size:48px;font-weight:700;color:var(--ink);letter-spacing:.5px}
.h2.light{color:var(--white)}
.btn{display:inline-block;border:2px solid var(--blue);color:var(--blue);border-radius:22px;
  font-size:15px;font-weight:700;padding:8px 26px;letter-spacing:.5px}
.btn.on-blue{border-color:var(--white);color:var(--white)}

/* vision */
.vision-title{left:104px;top:868px}
.vision-list{left:104px;top:948px;width:1010px;list-style:none}
.vision-list li{position:relative;padding-left:22px;font-size:15.5px;line-height:29.6px;color:var(--text)}
.vision-list li::before{content:"";position:absolute;left:0;top:11px;width:7px;height:7px;background:var(--blue)}
.vision-btn{left:104px;top:1488px}

/* value band */
.tile-label{font-size:17px;font-weight:700;color:var(--white);text-decoration:underline;letter-spacing:.5px}

/* mission */
.mission-title{left:760px;top:2318px}
.mission-list{left:106px;top:2462px;width:1000px;list-style:none}
.mission-list>li{position:relative;padding-left:22px;font-size:16px;line-height:28px}
.mission-list>li::before{content:"";position:absolute;left:0;top:10px;width:7px;height:7px;background:var(--blue)}
.mission-list ol{list-style:none;margin:10px 0 40px 60px}
.mission-list ol li{font-size:16px;line-height:34px}
.mission-list ol span{display:inline-block;width:40px;font-weight:700}
.mission-btn{left:904px;top:2734px}

/* team */
.team-title{left:106px;top:3030px}
.team-intro{left:106px;top:3118px;width:1000px;font-size:16px;line-height:24px;color:var(--white)}
.values{left:106px;top:3192px;width:1000px;list-style:none}
.values li{font-size:15.5px;line-height:30px;color:var(--white)}
.values b{font-weight:700}
.team-btn{left:106px;top:3408px}

/* ceo */
.ceo-name{left:52px;top:3728px;font-size:52px;font-weight:700;color:var(--ink)}
.ceo-role{left:52px;top:3796px;font-size:18px;font-weight:700;color:var(--ink)}
.ceo-bio{left:52px;top:3838px;width:530px;font-size:16px;line-height:23px;color:var(--text)}
.ceo-photo{left:600px;top:3590px;width:600px;height:800px;
  background:linear-gradient(180deg,#5a5048 0%,#9d8a7c 45%,#2e2d32 100%)}

/* contact */
.contact-title{left:106px;top:4548px}
.contact-sub{left:106px;top:4606px;font-size:17px;font-weight:700;color:var(--white)}
.addr-label{left:106px;top:4664px;font-size:16px;font-weight:700;color:var(--white);display:flex;align-items:center;gap:10px}
.addr{left:130px;top:4724px;font-size:16px;font-weight:700;line-height:30px;color:var(--white)}
.social{left:106px;top:4896px;display:flex;gap:22px}
.social span{width:24px;height:24px;border-radius:50%;background:var(--white)}
.field{background:var(--blue-dark);border:1px solid var(--field-line);color:var(--white);
  font-size:13px;padding:8px 10px}
.footer-copy{left:106px;top:5135px;font-size:13px;color:var(--white)}
.to-top{left:952px;top:5131px;font-size:13px;color:var(--white);display:flex;align-items:center;gap:14px}
</style>
</head>
<body>
<div class="page">

  <!-- hero -->
  <div class="abs hero-photo" role="img" aria-label="Photo of business people shaking hands over a desk with laptop and papers"></div>
  <div class="abs brand"><span class="brand-name">BrightWell</span><span class="brand-dot"></span></div>
  <nav class="abs nav"><a href="#vision">VISION</a><a href="#mission">MISSION</a><a href="#team">OUR TEAM</a><a href="#contact">CONTACT</a></nav>
  <h1 class="abs usp">WE HELP PEOPLE HELP THEMSELVES.</h1>
  <p class="abs motto"><b>“</b> BRIGHTWELL - DIRECT BRILLIANCE <b>”</b></p>

  <!-- vision panel -->
  <svg class="shape" style="top:560px" width="1200" height="1100" viewBox="0 0 1200 1100">
    <polygon points="0,40 1200,160 1200,1100 0,1100" fill="#ffffff" fill-opacity=".93"/>
  </svg>
  <svg class="abs chevron" width="60" height="30" viewBox="0 0 60 30"><polyline points="6,6 30,24 54,6" fill="none" stroke="#2e9fd9" stroke-width="3"/></svg>

  <section id="vision">
    <h2 class="abs h2 vision-title">OUR VISION</h2>
    <ul class="abs vision-list">
      <li>We are a direct response company that creates and sells information products and services that millions of people find interesting and important in their lives.</li>
      <li>We are specialized in the self-reliance market and we serve conservative Americans.</li>
      <li>We are in this business to serve globally and to grow individually.</li>
      <li>What we serve and inspire are people who need safety, comfort and peace of mind.</li>
      <li>We deliver empowerment through products that create fertile shortcuts to solutions, disentangle reality, simplify choices and ultimately make lives better.</li>
      <li>We give reassurance and confidence to these people through fresh, unique solutions.</li>
      <li>We get our inspiration from modern heroes and make their stories available for others.</li>
      <li>In a way we are democratizing wisdom because we solve serious problems shared by millions of people worldwide.</li>
      <li>We might not directly save lives, but we try to make a change. We help people help themselves.</li>
      <li>With our thirst for knowledge and drive for constant improvement, we know we'll find a solution to any challenge.</li>
      <li>And while doing that, we decided to water our inner seeds and harvest the best of our humanity.</li>
      <li>We invest time and energy in becoming better in the competition with ourselves.</li>
      <li>We believe that our better selves of tomorrow will nurture better tomorrows for others.</li>
    </ul>
    <span class="abs btn vision-btn">CONTACT NOW</span>
  </section>

  <!-- mission backdrop -->
  <div class="abs" style="left:0;top:1900px;width:1200px;height:1000px;background:linear-gradient(180deg,#dfe3e7 0%,#c7ccd2 50%,#e9ebee 100%)" role="img" aria-label="Faded photo of business people standing in an office"></div>
  <svg class="shape" style="top:2200px" width="1200" height="600" viewBox="0 0 1200 600">
    <polygon points="0,60 1200,0 1200,600 0,600" fill="#ffffff" fill-opacity=".9"/>
  </svg>

  <!-- value band -->
  <svg class="shape" style="top:1600px" width="1200" height="640" viewBox="0 0 1200 640">
    <polygon points="0,20 1200,190 1200,640 0,430" fill="#2e9fd9"/>
    <polygon points="240,54 480,88 480,520 240,472" fill="#c8bfae"/>
    <polygon points="720,122 950,155 950,600 720,560" fill="#8b857c"/>
    <polygon points="950,155 1200,190 1200,640 950,600" fill="#1f7fb8" fill-opacity=".85"/>
  </svg>
  <div class="abs" style="left:240px;top:1654px;width:240px;height:460px" role="img" aria-label="Photo of hands reviewing charts on paper"></div>
  <div class="abs" style="left:720px;top:1722px;width:230px;height:440px" role="img" aria-label="Photo of colleagues talking at a table"></div>
  <div class="abs" style="left:950px;top:1755px;width:250px;height:445px" role="img" aria-label="Blue-tinted photo of a team meeting"></div>
  <span class="abs tile-label" style="left:70px;top:1776px">FAIRNESS</span>
  <span class="abs tile-label" style="left:565px;top:1912px">SAFETY</span>
  <span class="abs tile-label" style="left:975px;top:2040px">UNCONDITIONED HELP</span>

  <section id="mission">
    <h2 class="abs h2 mission-title">OUR MISSION</h2>
    <ul class="abs mission-list">
      <li>We are masters of direct response marketing. Our expertise is three folded:
        <ol>
          <li><span>1.</span>We create and aggregate great information products.</li>
          <li><span>2.</span>We write content that compels people to act.</li>
          <li><span>3.</span>We do deep research to offer simple quick and easy solutions to people's most serious problems.</li>
        </ol>
      </li>
      <li>We create content and build solutions to profound challenges for millions of people.</li>
    </ul>
    <span class="abs btn mission-btn">CONTACT NOW</span>
  </section>

  <!-- team -->
  <svg class="shape" style="top:2740px" width="1200" height="860" viewBox="0 0 1200 860">
    <polygon points="0,110 1200,0 1200,860 0,800" fill="#2e9fd9"/>
    <polygon points="700,60 1200,14 1200,500 700,520" fill="#1f7fb8" fill-opacity=".35"/>
  </svg>
  <div class="abs" style="left:700px;top:2780px;width:500px;height:480px" role="img" aria-label="Blue-tinted photo of a hand writing on documents"></div>

  <section id="team">
    <h2 class="abs h2 light team-title">OUR TEAM &amp; VALUES</h2>
    <p class="abs team-intro">We're a small team of smart, funny hard-working specialists who are pushing to become the #1 company in self-reliance. High ambition, radical honesty and a result-oriented mindset are encouraged at BrightWell.</p>
    <ul class="abs values">
      <li><b>Impact</b> - leverage, maximum results, 80/20, greatness</li>
      <li><b>Wisdom</b> - learning mode "on", practice of self-improvement as a lifestyle</li>
      <li><b>Team spirit</b> - cooperation and complementarity, synergy, yin &amp; yang</li>
      <li><b>Courage</b> - feel the fear and do it anyway</li>
      <li><b>Innovation mindset</b> - you reconsider and reconnect things, so you can solve old problems in new, better ways</li>
      <li><b>Ownership</b> - "leaders must own everything in their world. There is no one else to blame"</li>
    </ul>
    <span class="abs btn on-blue team-btn">CONTACT NOW</span>
  </section>

  <!-- ceo -->
  <svg class="shape" style="top:3500px" width="1200" height="900" viewBox="0 0 1200 900">
    <polygon points="0,0 1200,90 1200,900 0,900" fill="#ffffff"/>
  </svg>
  <div class="abs ceo-photo" role="img" aria-label="Portrait photo of the company founder in a dark jacket"></div>
  <h2 class="abs ceo-name">MARIN DOVEL</h2>
  <p class="abs ceo-role">CEO BrightWell</p>
  <p class="abs ceo-bio">Marin started or was involved in 15 failed businesses before discovering online copywriting. After that, he ended up writing for Norvik Inc. and did 10-12 "successful" projects there, at least 3 of which broke the million-dollar mark. He wrote the famous HearthPower and the infamous CoilWisdom and Calder Motor sales letters. In 2012 Marin decided to start his own business, and to sell legit products he and his team could actually be proud of. Six months into the business they had Garden Freedom, a legendary aquaponics/survival food offer that did over 150,000 initial sales. Ever since, they've been doing successful survival offers, and are one of the few "survival" players constantly coming up with new offers.<br>Key personal strengths: copywriting, consulting, positioning, idea generation, mentoring.</p>

  <!-- contact -->
  <svg class="shape" style="top:4290px" width="1200" height="897" viewBox="0 0 1200 897">
    <polygon points="0,96 1200,0 1200,897 0,897" fill="#2e9fd9"/>
    <rect x="0" y="820" width="1200" height="1" fill="#ffffff" fill-opacity=".4"/>
  </svg>

  <section id="contact">
    <h2 class="abs h2 light contact-title">CONTACT US</h2>
    <p class="abs contact-sub">We Will Appreciate This Very Much</p>
    <p class="abs addr-label">
      <svg width="16" height="22" viewBox="0 0 16 22"><path d="M8 1a7 7 0 0 0-7 7c0 5 7 13 7 13s7-8 7-13a7 7 0 0 0-7-7z" fill="#fff"/><circle cx="8" cy="8" r="2.6" fill="#2e9fd9"/></svg>
      ADDRESS</p>
    <p class="abs addr">Suite 48 902 Lakeview Lane<br>Ashford 555-014-2279<br>This is a sample address</p>
    <div class="abs social" aria-label="Social links"><span></span><span></span><span></span><span></span></div>

    <div class="abs field" style="left:470px;top:4668px;width:258px;height:36px">Name</div>
    <div class="abs field" style="left:742px;top:4668px;width:270px;height:36px">Email</div>
    <div class="abs field" style="left:470px;top:4722px;width:258px;height:36px">Website</div>
    <div class="abs field" style="left:742px;top:4722px;width:270px;height:36px">Subject</div>
    <div class="abs field" style="left:470px;top:4776px;width:542px;height:188px">Message</div>
  </section>

  <p class="abs footer-copy">© 2016 BRIGHTWELL. All Rights Reserved.</p>
  <p class="abs to-top">BACK TO TOP
    <svg width="22" height="14" viewBox="0 0 22 14"><polyline points="2,12 11,3 20,12" fill="none" stroke="#fff" stroke-width="2"/></svg></p>

</div>
</body>
</html>
```